Web design for a food truck business

We need a web design for an established food truck business who have an active Facebook following but no website. We are a digital marketing agency and the client is looking for a website that stands out and doesn't have a corporate or boring look to it.
The client's facebook page is: https://www.facebook.com/DonTortaVelaroy/

Number of Pages Required

1 page

```html
<!DOCTYPE html>
<html lang="en">
<head>
<meta charset="utf-8">
<title>Rueda Tacos – A Food Truck Company</title>
<link href="https://fonts.googleapis.com/css2?family=Lato:wght@300;400;700;900&display=swap" rel="stylesheet">
<style>
:root{
  --topbar:#f1f1f1;
  --ink:#333;
  --brand-blue:#1a6fb5;
  --lime:#8dc63f;
  --lime-text:#9fd43a;
  --hero-top:#1d6bb8;
  --hero-bottom:#0c5a9f;
  --awning-red:#e8405a;
  --awning-cream:#f1ebc6;
  --badge-gold:#f2b933;
  --badge-red:#d63a3a;
  --navy:#030f26;
  --tile-1:#c2b8a3;
  --tile-2:#65a5bf;
  --tile-3:#4faf4f;
  --tile-4:#213b5e;
  --tile-5:#757779;
  --tile-6:#e0ab27;
}
*{margin:0;padding:0;box-sizing:border-box}
html,body{width:1200px;height:1200px;overflow:hidden}
body{position:relative;font-family:'Lato',sans-serif;color:var(--ink);background:var(--navy)}
.abs{position:absolute}

.topbar{left:0;top:0;width:1200px;height:36px;background:var(--topbar);font-size:9px;color:#555}
.topbar .contact{top:12px;display:flex;align-items:center;gap:5px}
.topbar .social{left:772px;top:7px;display:flex;gap:3px}
.topbar .social span{width:21px;height:21px;background:#fff;border:1px solid #e4e4e4;display:block}
.topbar .social span.active{background:#1aa3d8;border-color:#1aa3d8}
.topbar .lang{left:912px;top:12px;display:flex;align-items:center;gap:5px}
.flag{width:14px;height:9px;background:#6a7fb3;display:inline-block}

.header{left:0;top:36px;width:1200px;height:76px;background:#fff;border-bottom:1px solid #ddd}
.brand{left:246px;top:12px;display:flex;align-items:center;gap:12px}
.brand .mark{width:50px;height:50px;background:var(--brand-blue);border-radius:50%}
.brand .name{font-weight:900;font-size:21px;color:var(--brand-blue);line-height:1}
.brand .sub{font-weight:700;font-size:10.5px;color:var(--brand-blue);letter-spacing:.6px;margin-top:4px}
.nav{top:34px;font-size:8.5px;font-weight:700;color:#222;letter-spacing:-.1px}
.nav.current{color:var(--lime)}
.cta{left:966px;top:0;width:151px;height:76px;background:var(--lime);color:#fff;font-weight:900;font-size:12px;display:flex;align-items:center;justify-content:center}

.hero{left:0;top:112px;width:1200px;height:624px;background:linear-gradient(180deg,var(--hero-top),var(--hero-bottom))}
.awning{left:0;top:112px;width:1200px;height:48px;background:linear-gradient(180deg,var(--awning-red) 0%,#ee8a86 55%,var(--awning-cream) 100%)}
.cloud-edge{left:0;top:600px;width:1200px;height:136px;background:linear-gradient(180deg,rgba(255,255,255,0) 0%,rgba(255,255,255,.55) 55%,#fff 100%)}
.badge{left:234px;top:186px;width:142px;height:108px;border-radius:14px;background:linear-gradient(180deg,var(--badge-gold) 0%,#e98a3a 55%,var(--badge-red) 100%)}
.truck{left:652px;top:148px;width:372px;height:316px;border-radius:30px 30px 10px 10px;background:linear-gradient(180deg,#f1ece0 0%,#cfe0dc 50%,#72bcc7 100%)}
.tagline{top:296px;color:#fff;font-size:11px;letter-spacing:4.4px}
.dots{top:299px;display:flex;gap:3px}
.dots i{width:4px;height:4px;border-radius:50%;background:#2fe3c0;display:block}
.headline{left:236px;top:333px;color:#fff;font-size:50px;line-height:57px;font-weight:300;letter-spacing:-.8px}
.headline b{font-weight:900}

.grid{left:273px;top:466px;width:659px;height:218px;display:grid;grid-template-columns:repeat(3,1fr);grid-template-rows:1fr 1fr;box-shadow:0 8px 24px rgba(0,0,0,.25)}
.tile{color:#fff;text-align:center;padding-top:38px}
.tile h3{font-size:14px;font-weight:700;letter-spacing:-.4px}
.tile p{font-size:8.5px;margin-top:5px;letter-spacing:-.2px}

.about-label{left:236px;top:758px;color:var(--lime-text);font-size:11px;letter-spacing:-.3px}
.about-title{left:235px;top:779px;color:#fff;font-size:21px;font-weight:900;line-height:26px;letter-spacing:-.9px}
.about-motto{left:235px;top:857px;color:var(--lime-text);font-size:12px;font-weight:700;line-height:18px;letter-spacing:-.4px}
.about-copy{left:612px;top:762px;width:362px;color:#d7dbe3;font-size:10.8px;line-height:17.6px;letter-spacing:-.3px}
.about-copy p+p{margin-top:17.6px}

.stat{top:988px;display:flex;gap:16px;align-items:flex-start}
.stat svg{margin-top:10px}
.stat .num{color:#fff;font-size:25px;font-weight:900;letter-spacing:-1.2px;line-height:26px}
.stat .lbl{color:var(--lime-text);font-size:12px;letter-spacing:-.2px;margin-top:2px}

.work-title{left:0;top:1098px;width:1200px;text-align:center;color:#fff;font-size:26px;font-weight:900;letter-spacing:-.4px}
.work-sub{left:0;top:1135px;width:1200px;text-align:center;color:var(--lime-text);font-size:10px;font-style:italic;letter-spacing:-.3px}
.partners{left:236px;top:1183px;width:734px;height:17px;display:grid;grid-template-columns:repeat(3,1fr);gap:2px}
.partners span{background:#161a20}
</style>
</head>
<body>

<div class="abs topbar">
  <div class="abs contact" style="left:236px">
    <svg width="6" height="9" viewBox="0 0 6 9"><rect x=".5" y=".5" width="5" height="8" rx="1" fill="none" stroke="#7cc242"/></svg>
    (+1) 555 014 2280
  </div>
  <div class="abs contact" style="left:353px">
    <svg width="10" height="8" viewBox="0 0 10 8"><rect x=".5" y=".5" width="9" height="7" fill="none" stroke="#7cc242"/><path d="M.5 .5 5 4.5 9.5 .5" fill="none" stroke="#7cc242"/></svg>
    hello@ruedatacos.com
  </div>
  <div class="abs social"><span></span><span></span><span></span><span class="active"></span></div>
  <div class="abs lang"><i class="flag"></i>English
    <svg width="6" height="4" viewBox="0 0 6 4"><path d="M.5 .5 3 3 5.5 .5" fill="none" stroke="#777"/></svg>
  </div>
</div>

<header class="abs header">
  <div class="abs brand">
    <span class="mark"></span>
    <div><div class="name">Rueda Tacos</div><div class="sub">A Food Truck Company</div></div>
  </div>
  <span class="abs nav current" style="left:582px">HOME</span>
  <span class="abs nav" style="left:634px">ABOUT US</span>
  <span class="abs nav" style="left:700px">OUR MENU</span>
  <span class="abs nav" style="left:768px">SPOTS</span>
  <span class="abs nav" style="left:813px">TESTIMONIALS</span>
  <span class="abs nav" style="left:898px">CONTACT</span>
  <a class="abs cta">Contact Form</a>
</header>

<section class="abs hero"></section>
<div class="abs awning" role="img" aria-label="Striped red and cream scalloped awning"></div>
<div class="abs cloud-edge" role="img" aria-label="Soft white clouds closing the hero"></div>

<div class="abs badge" role="img" aria-label="Food truck menu badge"></div>
<div class="abs truck" role="img" aria-label="Illustrated food truck with branded roof sign"></div>

<div class="abs dots" style="left:234px"><i></i><i></i></div>
<div class="abs tagline" style="left:278px">A Professional Truck Food Company</div>
<div class="abs dots" style="left:622px"><i></i><i></i></div>
<h1 class="abs headline">We Deliver <b>Food</b><br>To <b>Everywhere.</b></h1>

<div class="abs grid">
  <div class="tile" style="background:var(--tile-1)"><h3>Featured Food 1</h3><p>Food Description Here</p></div>
  <div class="tile" style="background:var(--tile-2)"><h3>Featured Food 2</h3><p>Food Description Here</p></div>
  <div class="tile" style="background:var(--tile-3)"><h3>Featured Food 3</h3><p>Food Description Here</p></div>
  <div class="tile" style="background:var(--tile-4)"><h3>Featured Food 4</h3><p>Food Description Here</p></div>
  <div class="tile" style="background:var(--tile-5)"><h3>Featured Food 5</h3><p>Food Description Here</p></div>
  <div class="tile" style="background:var(--tile-6)"><h3>Featured Food 6</h3><p>Food Description Here</p></div>
</div>

<div class="abs about-label">About Rueda Tacos</div>
<h2 class="abs about-title">If you are looking for Professional<br>Food in open place, We can Help.</h2>
<div class="abs about-motto">Simple.<br>Yet, Revolutionary.</div>
<div class="abs about-copy">
  <p>We forge and find the best new ideas and proven practices from across our vast network of leaders. Then, in three critical areas, we provide you with the technology and consulting solutions needed to hardwire best practices.</p>
  <p>For more than 20 years in this industry, Northway Partners has helped 600+ agencies to analyze existing business operations and develop customized action plans for improvement and growth. We identify, understand and resolve critical day-to-day issues that are common in the agency environment. By helping clients embrace proven business management strategies, agency best practices and consistency in branding.</p>
</div>

<div class="abs stat" style="left:236px">
  <svg width="30" height="30" viewBox="0 0 30 30" fill="none" stroke="#fff" stroke-width="1.4"><path d="M3 12 9 5l6 4 6-4 6 7-10 11-4-4"/><path d="M9 15l5 5M12 12l5 5"/></svg>
  <div><div class="num">357</div><div class="lbl">Satisfied Clients</div></div>
</div>
<div class="abs stat" style="left:430px">
  <svg width="26" height="30" viewBox="0 0 26 30" fill="none" stroke="#fff" stroke-width="1.4"><circle cx="13" cy="9" r="6"/><path d="M2 28c0-7 5-11 11-11s11 4 11 11"/><path d="M10 24l3 3 5-5"/></svg>
  <div><div class="num">5</div><div class="lbl">Employees</div></div>
</div>
<div class="abs stat" style="left:616px">
  <svg width="26" height="30" viewBox="0 0 26 30" fill="none" stroke="#fff" stroke-width="1.4"><path d="M3 14h17v5a7 7 0 0 1-7 7h-3a7 7 0 0 1-7-7z"/><path d="M20 16h3v4h-3"/><path d="M1 29h22M9 5v5M12 5v5M15 5v5"/></svg>
  <div><div class="num">164</div><div class="lbl">Visited Spots</div></div>
</div>
<div class="abs stat" style="left:806px">
  <svg width="24" height="30" viewBox="0 0 24 30" fill="none" stroke="#fff" stroke-width="1.4"><path d="M7 10l-5 5 5 5M17 10l5 5-5 5M14 8l-4 14"/></svg>
  <div><div class="num">6243</div><div class="lbl">Served</div></div>
</div>

<h2 class="abs work-title">Our Work</h2>
<div class="abs work-sub">Companies that we are working with</div>
<div class="abs partners"><span></span><span></span><span></span></div>

</body>
</html>
```